Petal Sprite - web design for my new flower atelier

I would like to ask for design proposal for my newly established flower atelier. My brand name is Petal Sprite and I focus on realisation of events and flower projects (any kind) for physical as well as legel persons. I don’t operate as a standard flowershop. I would like to have 5 key parts - 1/Landing pg/welcome, 2/About me, 3/Gallery, 4/References, 5/Contact details. I would like the web design to reflect the way I am/ I do the things, ie, be slightly different, do non-tradiotional arrangements, my passion for flowers, gentle& fregile style, love for minimalism and details in the arrangements. I attach couple of photos of what I do so that you can better understand my style . You can see more on IG mirka_petal_sprite or FB Petal Sprite. I was wondering maybe one of the first 2 photos could be part of the landing pg. Or another idea is to have a design similar to this one https://thistlebloomstudio.example, ie to choose 3-5photos which are being animated like here. However, I am open to discuss any ideas and look forward for all the proposals.

Target Market(s)

physical as well as legal persons - weddings, celebrations, business events, projects for hotels, beaty salons, restaurants and others.. actually any kind of flower project

Industry/Entity Type

flowers

Number of Pages Required

1 page

Font styles to use
Other font styles liked:
• the font which matches the logo font style

Requirements
Must have
• to reflect the way I am as described above, I prefer more simple way of design, with the attention to a detail, I prefer pastel colours

```html
<!DOCTYPE html>
<html lang="en">
<head>
<meta charset="utf-8">
<title>Petal Sprite</title>
<link rel="stylesheet" href="https://fonts.googleapis.com/css2?family=Lato:wght@300;400;700&family=Pacifico&display=swap">
<style>
:root{
  --ink:#3f3b36;
  --muted:#5b5750;
  --brown:#8a7652;
  --button:#8c7f5c;
  --cream:#f0e8b9;
  --white:#ffffff;
  --ghost:#efefef;
  --line:#b9b2a3;
}
*{margin:0;padding:0;box-sizing:border-box}
html,body{width:1200px;height:2799px;overflow:hidden;background:var(--white)}
body{position:relative;font-family:"Lato",sans-serif;color:var(--ink)}
.abs{position:absolute}
.site-header{left:0;top:0;width:1200px;height:76px;background:var(--white)}
.brand-badge{left:179px;top:-66px;width:229px;height:229px;border-radius:50%;background:var(--white);z-index:3;display:flex;align-items:flex-end;justify-content:center;padding-bottom:50px}
.brand-name{font-family:"Lato",sans-serif;font-weight:400;font-size:27px;color:var(--brown);letter-spacing:1px}
.main-nav{left:587px;top:33px;display:flex;gap:30px;font-size:11px;font-weight:700;color:var(--ink);z-index:4}
.hero{left:0;top:76px;width:1200px;height:509px;
  background:linear-gradient(90deg,#ebebe9 0%,#e3e4df 13%,#a9b78f 22%,#5f7a38 33%,#3f5726 48%,#55702f 62%,#7f9a55 74%,#c9cfbd 84%,#e6e6e3 92%,#ececea 100%)}
.vine{left:14px;top:588px;width:226px;height:516px;background:linear-gradient(180deg,#faf8f4,#f3eee4 50%,#faf8f4)}
.intro-text{left:252px;top:746px;width:298px;font-size:12.5px;font-weight:300;line-height:20px;color:var(--ink)}
.btn-outline{left:251px;top:989px;width:130px;height:31px;border:1px solid #c9a77b;color:#b0895a;font-size:10.5px;font-weight:700;display:flex;align-items:center;justify-content:center}
.vertical-word{font-family:"Pacifico",cursive;transform:rotate(-90deg);transform-origin:left top;white-space:nowrap}
.welcome-word{left:548px;top:1022px;font-size:66px;color:var(--ghost);line-height:1}
.photo-tall{left:632px;top:685px;width:249px;height:375px;background:linear-gradient(180deg,#f3f3f1 0%,#ededeb 55%,#e2e2df 100%)}
.photo-short{left:895px;top:723px;width:199px;height:298px;background:linear-gradient(180deg,#d9d9d7,#e3e3e1 60%,#d6d6d3)}
.help{left:0;top:1104px;width:1200px;height:533px;background:var(--cream)}
.help-title{left:0;top:1170px;width:1200px;text-align:center;font-family:"Pacifico",cursive;font-weight:400;font-size:30px;color:#4d4945}
.help-sub{left:0;top:1229px;width:1200px;text-align:center;font-size:12.5px;font-weight:300;color:var(--ink)}
.event-photo{top:1275px;height:230px}
.photo-wedding{left:253px;width:338px;background:linear-gradient(180deg,#3c5330 0%,#6f8760 25%,#d9dfd0 45%,#8a6a4c 70%,#4a3526 100%)}
.photo-corporate{left:610px;width:341px;background:linear-gradient(180deg,#efe3d3 0%,#eedfd8 40%,#e3b9c3 65%,#efe5e0 100%)}
.caption{font-size:16px;font-weight:300;color:var(--muted);text-align:center}
.contact-band{left:0;top:1641px;width:1200px;height:382px;background:linear-gradient(90deg,#b07d22 0%,#8a5a1c 18%,#6c4216 30%,#b8955e 48%,#d9c39b 55%,#9a6a28 68%,#5a3814 82%,#a47224 100%)}
.contact-word{left:160px;top:1990px;font-size:66px;color:var(--white);line-height:1}
.contact-card{left:239px;top:1728px;width:233px;height:258px;background:var(--white);border:2px solid #3c3a36;padding:48px 22px 0 23px}
.contact-card p.lead{font-size:14px;font-weight:300;line-height:19.5px;color:var(--ink)}
.contact-card p.note{margin-top:12px;font-size:10.5px;line-height:17px;color:#8a857c}
.btn-solid{background:var(--button);color:var(--white);font-size:10.5px;font-weight:700;display:flex;align-items:center;justify-content:center}
.contact-btn{margin-top:16px;width:97px;height:25px}
.insta-word{left:0;top:2060px;width:1200px;text-align:center;font-family:"Pacifico",cursive;font-size:72px;color:#f3f3f3;line-height:1.3}
.feed-photo{top:2156px;width:249px;height:247px}
.feed-1{left:90px;background:linear-gradient(90deg,#5a3f26 0%,#c9a233 35%,#b8872a 60%,#4a3422 100%)}
.feed-2{left:351px;background:linear-gradient(180deg,#b7afa3 0%,#a4362c 40%,#c77a2b 60%,#4a4440 100%)}
.feed-3{left:612px;background:linear-gradient(180deg,#8f5640 0%,#c98a86 45%,#a89f95 75%,#c9a778 100%)}
.feed-4{left:876px;background:linear-gradient(90deg,#9a5e3e 0%,#3f5a33 45%,#2f4a28 55%,#b07a52 100%)}
.follow-btn{left:509px;top:2424px;width:204px;height:36px;font-size:12.5px}
.footer-rule{top:2595px;height:1px;background:var(--line)}
.rule-left{left:43px;width:477px}
.rule-right{left:659px;width:520px}
.footer-circle{left:548px;top:2544px;width:92px;height:92px;border:1.5px solid var(--brown);border-radius:50%}
.footer-name{left:0;top:2645px;width:1200px;text-align:center;font-size:32px;font-weight:400;color:var(--brown);letter-spacing:1px}
.socials{left:0;top:2709px;width:1200px;display:flex;justify-content:center;gap:44px;font-size:11.5px;font-weight:400;color:var(--ink)}
.copyright{left:0;top:2738px;width:1200px;text-align:center;font-size:11px;color:var(--ink)}
</style>
</head>
<body>
<header class="site-header abs"></header>
<div class="brand-badge abs"><span class="brand-name">Petal Sprite</span></div>
<nav class="main-nav abs"><span>Home</span><span>About Petal Sprite</span><span>Gallery</span><span>References</span><span>Contact</span></nav>

<div class="hero abs" role="img" aria-label="Green tulip and thistle arrangement in a dark stone vase on snow"></div>

<section>
  <div class="vine abs" role="img" aria-label="Line illustration of a flowering vine"></div>
  <p class="intro-text abs">Floristry can involve the cultivation of flowers as well as their arrangement, and to the business of selling them. Much of the raw material supplied for the floristry trade comes from the cut flowers industry. Florist shops are the main flower-only outlets, but supermarkets, garden supply stores also sell flowers.Customer satisfaction is our number one priority, and we strive to stand apart from the competition by providing you with fresh flowers and unique designs that are sure to put a smile on every recipient's face.</p>
  <div class="btn-outline abs">Read more about us</div>
  <div class="vertical-word welcome-word abs">Welcome.</div>
  <div class="photo-tall abs" role="img" aria-label="Curly willow and yellow blooms in a green bottle vase"></div>
  <div class="photo-short abs" role="img" aria-label="Smaller view of the willow arrangement in a green vase"></div>
</section>

<section class="help abs"></section>
<h2 class="help-title abs">How can we help?</h2>
<p class="help-sub abs">Email us at help@petalsprite.example to schedule your wedding or event consultation</p>
<div class="event-photo photo-wedding abs" role="img" aria-label="Wedding tables decorated with white flowers outdoors"></div>
<div class="event-photo photo-corporate abs" role="img" aria-label="Banquet hall with pink floral centerpieces"></div>
<p class="caption abs" style="left:253px;width:338px;top:1523px">Weddings</p>
<p class="caption abs" style="left:610px;width:341px;top:1520px">Corporate Business events</p>

<section class="contact-band abs" role="img" aria-label="Close-up of flowering branches in warm light"></section>
<div class="vertical-word contact-word abs">contact.</div>
<div class="contact-card abs">
  <p class="lead">Petal Sprite offer nature-inspired floral design for weddings and special events.</p>
  <p class="note">Email us at help@petalsprite.example for inquiries.</p>
  <div class="btn-solid contact-btn">Contact Us</div>
</div>

<div class="insta-word abs">Snapgrid.</div>
<div class="feed-photo feed-1 abs" role="img" aria-label="Small bouquet in a pink vase beside a yellow armchair"></div>
<div class="feed-photo feed-2 abs" role="img" aria-label="Two colourful mixed bouquets in glass vases"></div>
<div class="feed-photo feed-3 abs" role="img" aria-label="Protea arrangement in a stone vase"></div>
<div class="feed-photo feed-4 abs" role="img" aria-label="Bird of paradise arrangement against a brick wall"></div>
<div class="btn-solid follow-btn abs">Follow us on snapgrid</div>

<footer>
  <div class="footer-rule rule-left abs"></div>
  <div class="footer-rule rule-right abs"></div>
  <div class="footer-circle abs"></div>
  <div class="footer-name abs">Petal Sprite</div>
  <div class="socials abs"><span>Snapgrid</span><span>Friendsheet</span><span>Pinboardly</span><span>Worklink</span></div>
  <p class="copyright abs">© 2022, PetalSprite. All Right Reserved</p>
</footer>
</body>
</html>
```